Professional Business Card for Commercial Cleaning Company

We need a business card that represents our commercial janitorial cleaning company and represent several brands for our company so we do not want to highlight the logo too much. We want something that says we are professional.
Notes:No website or address as we have many locations and many websites and companies under our corporate name of "Brightwell Holdings, LLC" . Every time we hand a customer a business card they have contacted us via another brand we own but we don't want to have 21 business cards so we want to not focus on Brightwell Holdings, LLC too much since people will automatically ask "What is Brightwell Holdings, LLC" Example: Noodle Barn and Wrap Dome restaurants are owned by "Zing! Brands" is the corporation name. Same principle here. Except we do not advertise at this time that all of our brands are connected. Hope this helps.
Target Market(s)
Commercial Cleaning
Industry/Entity Type
Janitorial Service
Contact Information for Business Card
Miles Hartwin
Business Development
347-628-9043
sales@brightwellholdingsllc.example
Requirements
Must have
- Logo with contact information, need to be able to easily edit contact info for others in my office.
Nice to have
- Professional Image. Like to see a colorful bold look and a more standard business card look.
Should not have
- Any type of cleaning icons, tools, people or water.

```html
<!DOCTYPE html>
<html lang="en">
<head>
<meta charset="utf-8">
<title>Brightwell Holdings, LLC — Business Card</title>
<link rel="stylesheet" href="https://fonts.googleapis.com/css2?family=Montserrat:wght@600;700&family=Roboto:wght@400&display=swap">
<style>
  :root {
    --navy: #0a3a7a;
    --navy-deep: #07336d;
    --green: #6aa83a;
    --ink: #4a4a4a;
    --rule: #b9b9b9;
    --paper: #ffffff;
    --backdrop: #eef0f2;
  }
  * { box-sizing: border-box; margin: 0; padding: 0; }
  html, body {
    width: 1200px; height: 711px; overflow: hidden;
    background: var(--backdrop);
  }
  .canvas {
    position: relative; width: 1200px; height: 711px;
    display: flex; align-items: center; justify-content: center; gap: 40px;
  }
  .card {
    position: relative; width: 540px; height: 309px; overflow: hidden;
    box-shadow: 0 6px 18px rgba(0, 0, 0, 0.12);
  }
  .card-front { background: var(--paper); }
  .front-frame {
    position: absolute; inset: 14px;
    border: 3px solid var(--navy);
  }
  .brand-name {
    position: absolute; left: 38px; top: 148px;
    font-family: "Montserrat", sans-serif; font-weight: 600;
    font-size: 15px; color: var(--navy); white-space: nowrap;
  }
  .divider {
    position: absolute; left: 258px; top: 100px;
    width: 1px; height: 110px; background: var(--rule);
  }
  .contact {
    position: absolute; left: 272px; top: 110px;
    width: 236px;
  }
  .contact-name {
    font-family: "Montserrat", sans-serif; font-weight: 700;
    font-size: 20px; color: var(--navy); line-height: 1.1;
  }
  .contact-title {
    font-family: "Montserrat", sans-serif; font-weight: 600;
    font-size: 13px; color: var(--green); margin-top: 2px; margin-bottom: 8px;
  }
  .contact-line {
    display: flex; align-items: center; gap: 7px;
    font-family: "Roboto", sans-serif; font-size: 11.5px;
    color: var(--ink); line-height: 20px; white-space: nowrap;
  }
  .contact-line svg { flex: none; }
  .card-back { background: var(--navy-deep); }
  .back-brand {
    position: absolute; right: 40px; bottom: 58px;
    font-family: "Montserrat", sans-serif; font-weight: 600;
    font-size: 22px; color: var(--paper); white-space: nowrap;
  }
</style>
</head>
<body>
<main class="canvas">
  <section class="card card-front" aria-label="Business card front">
    <div class="front-frame"></div>
    <div class="brand-name">Brightwell Holdings, LLC</div>
    <div class="divider"></div>
    <div class="contact">
      <div class="contact-name">Miles Hartwin</div>
      <div class="contact-title">Business Development</div>
      <div class="contact-line">
        <svg width="10" height="14" viewBox="0 0 10 14" aria-hidden="true">
          <rect x="1" y="0.75" width="8" height="12.5" rx="1.3" fill="none" stroke="var(--navy)" stroke-width="1.5"/>
          <line x1="3.5" y1="11" x2="6.5" y2="11" stroke="var(--navy)" stroke-width="1.2"/>
        </svg>
        <span>347-628-9043</span>
      </div>
      <div class="contact-line">
        <svg width="12" height="10" viewBox="0 0 12 10" aria-hidden="true">
          <rect x="0" y="1" width="12" height="9" rx="1" fill="var(--navy)"/>
          <polyline points="0.8,2 6,6 11.2,2" fill="none" stroke="#fff" stroke-width="1.2"/>
        </svg>
        <span>sales@brightwellholdingsllc.example</span>
      </div>
    </div>
  </section>

  <section class="card card-back" aria-label="Business card back">
    <div class="back-brand">Brightwell Holdings, LLC</div>
  </section>
</main>
</body>
</html>
```